Security doors and flyscreens

We need business cards for our company called K & R Traders. We quote, manufacture and install security doors and flyscreens.

Industry/Entity Type

Security

Contact Information for Business Card

K & R TRADERS
17 Larkfield Ave. Ashgrove Park 3099
Ph: 8127 5506
Fax: 8127 5502
Colin: 0417 952 160
Email: gatemakerhub@mailbox-example.net

```html
<!DOCTYPE html>
<html lang="en">
<head>
<meta charset="utf-8">
<title>K &amp; R Traders – Business Card</title>
<link href="https://fonts.googleapis.com/css2?family=Lato:wght@400;700;900&display=swap" rel="stylesheet">
<style>
  :root {
    --page-bg: #1c1c1d;
    --panel-dark: #2a2a2c;
    --panel-dark-edge: #222224;
    --text-light: #f4f4f4;
    --photo-brick: #9c9a8e;
    --photo-siding: #bdb7ab;
    --photo-mesh: #5d5f5e;
    --photo-deck: #6b5648;
    --photo-frame: #cfc6b8;
  }
  * { box-sizing: border-box; margin: 0; padding: 0; }
  html, body {
    width: 1200px; height: 1000px; overflow: hidden;
    background: var(--page-bg);
  }
  .business-card {
    position: absolute;
    left: 100px; top: 214px;
    width: 1000px; height: 572px;
    display: flex;
    box-shadow: 0 20px 50px rgba(0,0,0,.6);
  }
  .photo-collage {
    position: relative;
    width: 440px; height: 100%;
    flex: none;
  }
  .photo { position: absolute; }
  .photo-lock { left: 0; top: 0; width: 190px; height: 200px;
    background: linear-gradient(135deg, var(--photo-mesh), var(--photo-siding)); }
  .photo-front-door { left: 190px; top: 0; width: 250px; height: 340px;
    background: linear-gradient(160deg, var(--photo-brick), #7d7b70 60%, var(--photo-mesh)); }
  .photo-open-door { left: 0; top: 200px; width: 250px; height: 372px;
    background: linear-gradient(150deg, var(--photo-siding), var(--photo-frame) 45%, var(--photo-deck)); }
  .photo-hinge { left: 250px; top: 340px; width: 190px; height: 232px;
    background: linear-gradient(120deg, #8d8478, var(--photo-frame) 55%, #4a4542); }

  .info-panel {
    flex: 1;
    background: radial-gradient(ellipse at 40% 30%, #323234, var(--panel-dark) 60%, var(--panel-dark-edge));
    color: var(--text-light);
    font-family: "Lato", sans-serif;
    text-align: center;
    padding: 56px 40px 0 20px;
  }
  .company-name {
    font-family: "Lato", sans-serif;
    font-weight: 900;
    font-size: 58px;
    letter-spacing: 2px;
    line-height: 1;
    color: var(--text-light);
  }
  .tagline {
    margin-top: 24px;
    font-weight: 700;
    font-size: 19px;
    line-height: 1.2;
  }
  .contact-list {
    list-style: none;
    margin-top: 46px;
    font-size: 20px;
    line-height: 1.35;
  }
  .contact-list .label { font-weight: 700; }
  .address {
    margin-top: 44px;
    font-size: 20px;
  }
</style>
</head>
<body>
  <article class="business-card">
    <section class="photo-collage">
      <div class="photo photo-lock" role="img" aria-label="Close-up of a security door lock on a diamond grille door"></div>
      <div class="photo photo-front-door" role="img" aria-label="Security screen door fitted in a brick wall entrance"></div>
      <div class="photo photo-open-door" role="img" aria-label="Open white security door with diamond mesh beside weatherboard wall"></div>
      <div class="photo photo-hinge" role="img" aria-label="Close-up of a black hinge on a door frame"></div>
    </section>
    <section class="info-panel">
      <h1 class="company-name">K &amp; R TRADERS</h1>
      <p class="tagline">We Quote, Manufacture and Install<br>Security Doors and Flyscreens.</p>
      <ul class="contact-list">
        <li><span class="label">P:</span> 8127 5506</li>
        <li><span class="label">F:</span> 8127 5502</li>
        <li><span class="label">M:</span> 0417 952 160 (Colin)</li>
        <li><span class="label">E:</span> gatemakerhub@mailbox-example.net</li>
      </ul>
      <p class="address">17 Larkfield Ave. Ashgrove Park 3099</p>
    </section>
  </article>
</body>
</html>
```